Design a brand style for my candle

Hi!
We need a label design created to start off our candle company, we look to create a fun, girly, cool and on trend brand. We are wanting a label to go on candles with a quote on it "Glow Softly". Please use this quote when submitting your design, if you could place it on a candle that would be awesome. We love the pastel colours of pink, how this is incorporated in other colours we look forward to your designs. I have attached photos as a start of a "mood board" . The font and style must be easily changed to suit other quotes and sayings
Thanks so much!
Updates

Looking for something modern, minimalist, cool and on Trend packaging targeting 20's women Added Thursday, January 5, 2017

Target Market(s)

Women 20-35
Style - Fun, Flirty, Clean Lines and Cool

Industry/Entity Type

Retail

Font styles to use
Sans Serif

Requirements
Must have
• pastel pink, the quote "Glow Softly" on the candle (pic is an example only, please do not use the same font)

```html
<!DOCTYPE html>
<html lang="en">
<head>
<meta charset="utf-8">
<title>Glow Softly — candle label</title>
<link rel="stylesheet" href="https://fonts.googleapis.com/css2?family=Playfair+Display:wght@500&display=swap">
<style>
  :root {
    --page-bg: #ffffff;
    --label-pink: #efb6dc;
    --label-mid: #f6d6ea;
    --label-white: #ffffff;
    --name-ink: #1c1a1c;
  }
  html, body {
    margin: 0;
    padding: 0;
    width: 1200px;
    height: 1200px;
    overflow: hidden;
    background: var(--page-bg);
  }
  .canvas {
    position: relative;
    width: 1200px;
    height: 1200px;
  }
  .label {
    position: absolute;
    left: 100px;
    top: 330px;
    width: 1000px;
    height: 540px;
    background: linear-gradient(90deg, var(--label-pink) 0%, var(--label-mid) 45%, var(--label-white) 92%);
    display: flex;
    align-items: center;
    justify-content: center;
    overflow: hidden;
  }
  .label__name {
    margin: 0;
    font-family: "Playfair Display", Georgia, serif;
    font-weight: 500;
    font-size: 110px;
    line-height: 1;
    letter-spacing: 0.06em;
    color: var(--name-ink);
    white-space: nowrap;
  }
</style>
</head>
<body>
  <main class="canvas">
    <section class="label" aria-label="Glow Softly candle label">
      <p class="label__name">Glow Softly</p>
    </section>
  </main>
</body>
</html>
```